"The Orignal LoopTabs" needs a Package Design!! Everybody's got a LoopTab, What's Yours?

I need eye popping packaging design!! My LoopTabs are gonna be big! I'm a single mom I'm based in AZ, so this is big for me. The LoopTabs keep towels off the floor & so much more!! Color cardboard insert background, bright yellow and Bright blue, like a caribbean blue, funky font for the Product Name. The Original, can be smaller and in an easy script. I have some pictures so you can get an concept and basic design ideas. There are no limits to their uses!! Please call me for any questions or direction.
Updates

I want to thank you all for participating, You each brought a different perspective and had some really good ideas. I will definitely us this service again! Thank you, Dolores Fitchley

Target Market(s)

Mom's, woman, men, students you name it!!

Colors
fbee3e
0293ce

Requirements
Must have
• Clear pvc packaging so you can see the product and they have to hang over so you see how they are used. The look needs to draw people in to it!! Read my instructions on the downloaded pics and info and if you have questions please let me know. The towel and towel bar can be like a drawing not actual towel picture. On the reverse side is a list of ideas and my website. Other colors for lettering aside from the Caribbean blue for the word "LoopTabs" is up to you, use your expertise.
Should not have
• The blue is not on the color wheel that is shown here.

```html
<!DOCTYPE html>
<html lang="en">
<head>
<meta charset="utf-8">
<title>The Orignal LoopTabs – Package Design</title>
<link rel="stylesheet" href="https://fonts.googleapis.com/css2?family=Amatic+SC:wght@400;700&display=swap">
<style>
  :root {
    --yellow: #fbee3e;
    --yellow-light: #fdf68e;
    --blue: #0293ce;
    --caribbean: #22b5c8;
    --aqua-light: #b9e7ef;
    --ink: #2b2b2b;
    --grey: #555;
    --page-top: #ffffff;
    --page-bottom: #dcdcdc;
    --line: #6b6b6b;
  }
  * { box-sizing: border-box; margin: 0; padding: 0; }
  html, body { width: 1200px; height: 1200px; overflow: hidden; }
  body {
    position: relative;
    font-family: "Amatic SC", cursive;
    background: linear-gradient(180deg, var(--page-top) 0%, var(--page-bottom) 100%);
    color: var(--ink);
  }
  .abs { position: absolute; }

  /* Brand lockup */
  .brand { position: absolute; color: var(--caribbean); font-weight: 700; line-height: 1; white-space: nowrap; }
  .brand-small { display: block; font-size: 0.22em; margin-left: 0.9em; }
  .brand-main { display: block; }
  .hero-brand { left: 110px; top: 255px; font-size: 150px; }
  .hero-brand .brand-small { font-size: 30px; margin-left: 140px; margin-bottom: -14px; }

  /* Package panels */
  .panel { position: absolute; width: 366px; height: 436px; overflow: hidden; }
  .panel-front { background: radial-gradient(ellipse at 45% 45%, var(--yellow-light) 0%, var(--yellow) 70%); }
  .panel-back { background: linear-gradient(180deg, var(--aqua-light) 0%, #5ccbe0 40%, var(--caribbean) 100%); }
  .front-large { left: 645px; top: 135px; transform: scale(1.095); transform-origin: top left; }
  .front-flat { left: 36px; top: 676px; }
  .back-flat { left: 430px; top: 676px; }

  .corner-sweep { position: absolute; inset: 0; }
  .corner-question { right: 8px; top: 8px; text-align: right; font-size: 16px; line-height: 0.95; color: var(--grey); }
  .corner-arrow { right: 10px; top: 48px; }

  .front-brand { left: 60px; top: 18px; font-size: 76px; }
  .front-brand .brand-small { font-size: 15px; margin-left: 72px; margin-bottom: -6px; }

  .slot { position: absolute; height: 2px; background: rgba(255,255,255,0.8); }
  .product-window {
    position: absolute; left: 78px; top: 128px; width: 222px; height: 210px;
    background: linear-gradient(90deg, #8fd14f 0%, #8fd14f 35%, #e8337f 45%, #e8337f 100%);
    border-radius: 4px 4px 40px 40px;
  }
  .towel-icon { left: 34px; top: 370px; width: 48px; height: 46px; background: var(--caribbean); border-radius: 2px 2px 10px 10px; }
  .tagline { font-size: 19px; line-height: 0.95; color: var(--grey); font-weight: 700; }
  .tagline-a { left: 96px; top: 380px; text-align: right; }
  .tagline-amp { left: 192px; top: 372px; font-size: 38px; color: var(--grey); }
  .tagline-b { left: 216px; top: 380px; }
  .tagline-arrow { left: 268px; top: 378px; }

  /* Back panel */
  .back-kicker { width: 100%; top: 28px; text-align: center; font-size: 26px; color: var(--ink); }
  .back-title { width: 100%; top: 56px; text-align: center; font-size: 44px; font-weight: 700; color: var(--ink); }
  .back-window {
    position: absolute; left: 120px; top: 130px; width: 140px; height: 40px;
    background: linear-gradient(90deg, #e8337f 0%, #e8337f 50%, #8fd14f 60%, #8fd14f 100%);
  }
  .ideas { list-style: none; font-size: 13px; line-height: 1.16; color: var(--ink); font-weight: 700; }
  .ideas li::before { content: "» "; }
  .ideas-a { left: 42px; top: 186px; }
  .ideas-b { left: 146px; top: 186px; }
  .contest { left: 248px; top: 186px; width: 100px; text-align: center; font-size: 13px; line-height: 1.16; font-weight: 700; color: var(--ink); }
  .win-badge {
    left: 262px; top: 240px; width: 60px; height: 60px; border-radius: 50%;
    background: #fff; display: flex; align-items: center; justify-content: center;
    text-align: center; font-size: 17px; line-height: 0.95; font-weight: 700; color: var(--ink);
  }
  .back-limit { width: 100%; top: 300px; text-align: center; font-size: 20px; font-weight: 700; color: var(--ink); }
  .back-brand { left: 100px; top: 328px; font-size: 56px; color: var(--yellow); }
  .back-brand .brand-small { font-size: 12px; margin-left: 56px; margin-bottom: -4px; }
  .back-url { width: 100%; top: 400px; text-align: center; font-size: 19px; color: #1d5f80; font-weight: 700; }

  /* Die-cut */
  .die-cut { left: 815px; top: 695px; width: 348px; height: 400px; background: #fff; border: 1px solid var(--line); }

  /* Captions */
  .caption { top: 1122px; font-size: 38px; color: var(--ink); text-align: center; }
  .caption-front { left: 36px; width: 366px; }
  .caption-back { left: 430px; width: 366px; }
  .caption-die { left: 815px; width: 348px; }
</style>
</head>
<body>

  <div class="brand hero-brand">
    <span class="brand-small">The Orignal</span>
    <span class="brand-main">LoopTabs</span>
  </div>

  <!-- Front panel, large -->
  <section class="panel panel-front front-large">
    <svg class="corner-sweep" viewBox="0 0 366 436" aria-hidden="true"><path d="M225 0 H366 V230 Q352 70 225 0 Z" fill="#ffffff"/></svg>
    <div class="abs corner-question">What's your<br>LoopTab?</div>
    <svg class="abs corner-arrow" width="22" height="18" viewBox="0 0 22 18" aria-hidden="true"><path d="M2 2 Q8 12 16 12 L14 7 L21 14 L12 17 L14 14 Q6 14 2 2 Z" fill="var(--caribbean)"/></svg>
    <div class="brand front-brand"><span class="brand-small">The Orignal</span><span class="brand-main">LoopTabs</span></div>
    <div class="slot" style="left:88px; top:128px; width:240px;"></div>
    <div class="product-window" role="img" aria-label="Green and pink LoopTab straps with white clips shown through the clear window"></div>
    <div class="abs towel-icon" role="img" aria-label="Drawing of a towel hanging from a bar with LoopTabs"></div>
    <div class="abs tagline tagline-a">No more towels<br>on the floor</div>
    <div class="abs tagline-amp">&amp;</div>
    <div class="abs tagline tagline-b">So much<br>more!</div>
    <svg class="abs tagline-arrow" width="52" height="32" viewBox="0 0 52 32" aria-hidden="true"><path d="M2 28 Q20 14 36 12 L34 4 L50 14 L36 28 L36 20 Q20 20 2 28 Z" fill="var(--caribbean)"/></svg>
  </section>

  <!-- Front panel -->
  <section class="panel panel-front front-flat">
    <svg class="corner-sweep" viewBox="0 0 366 436" aria-hidden="true"><path d="M225 0 H366 V230 Q352 70 225 0 Z" fill="#ffffff"/></svg>
    <div class="abs corner-question">What's your<br>LoopTab?</div>
    <svg class="abs corner-arrow" width="22" height="18" viewBox="0 0 22 18" aria-hidden="true"><path d="M2 2 Q8 12 16 12 L14 7 L21 14 L12 17 L14 14 Q6 14 2 2 Z" fill="var(--caribbean)"/></svg>
    <div class="brand front-brand"><span class="brand-small">The Orignal</span><span class="brand-main">LoopTabs</span></div>
    <div class="slot" style="left:88px; top:128px; width:240px;"></div>
    <div class="product-window" role="img" aria-label="Green and pink LoopTab straps with white clips shown through the clear window"></div>
    <div class="abs towel-icon" role="img" aria-label="Drawing of a towel hanging from a bar with LoopTabs"></div>
    <div class="abs tagline tagline-a">No more towels<br>on the floor</div>
    <div class="abs tagline-amp">&amp;</div>
    <div class="abs tagline tagline-b">So much<br>more!</div>
    <svg class="abs tagline-arrow" width="52" height="32" viewBox="0 0 52 32" aria-hidden="true"><path d="M2 28 Q20 14 36 12 L34 4 L50 14 L36 28 L36 20 Q20 20 2 28 Z" fill="var(--caribbean)"/></svg>
  </section>

  <!-- Back panel -->
  <section class="panel panel-back back-flat">
    <div class="abs back-kicker">Everybody's got a LoopTab,</div>
    <div class="abs back-title">What's yours?</div>
    <div class="slot" style="left:60px; top:128px; width:250px;"></div>
    <div class="back-window" role="img" aria-label="Pink and green LoopTab straps seen from the back"></div>
    <ul class="abs ideas ideas-a">
      <li>Baby quick fixes</li><li>Camping</li><li>College dorm rooms</li><li>Laundry</li>
      <li>Hanging items to dry</li><li>Working out at the gym</li><li>Traveling</li>
    </ul>
    <ul class="abs ideas ideas-b">
      <li>Home decorating</li><li>Kitchen</li><li>No-sew projects</li><li>Bathroom</li>
      <li>Pets</li><li>Clothing quick fix</li><li>Endless possibilities</li>
    </ul>
    <p class="abs contest">Endless uses - post a picture of your LoopTab idea to our website and</p>
    <div class="abs win-badge">You could<br>win!</div>
    <div class="abs back-limit">The only limit is your imagination!</div>
    <div class="brand back-brand"><span class="brand-small">The Orignal</span><span class="brand-main">LoopTabs</span></div>
    <div class="abs back-url">LoopTabsShop.com</div>
  </section>

  <div class="abs die-cut" role="img" aria-label="Die-cut template outline of the box with side flaps and hang slots"></div>

  <div class="abs caption caption-front">Front</div>
  <div class="abs caption caption-back">Back</div>
  <div class="abs caption caption-die">Die-Cut Template</div>

</body>
</html>
```